LuMen Assembly. "Powering Enterprise Renewal" Website

I have established a new company based in Sydney Australia that exists to support large service companies to transform their businesses. I offer a bespoke alternative to the large consulting firms like QR, Ferrander, WHTC and Bramwell. My intention over time is to grow this business with more consulting partners and practitioners and expand into ASIA PAC, Europe and the US.

I would like to create a mobile responsive website that has a similar look and feel to QR, see URL below plus URLs for Bramwell, Ferrander and WHTC.

http://www.qr-example.com/
https://home.whtc-example.com/au/en/home.html
http://www.bramwell-example.com/

I am on a limited budget however so do not require a whole lot of fancy features. Key priorities;

- Responsive to all device types. PC, Tablet, Mobile
- A horizontal scrolling set of hero images that link to particular story or subject like QR-example.com. 3 only required
- Only limited content is required and most would be static apart from hero scrolling images/topics at top of page
- I would need the ability to be able to remove, replace, update the hero slides every 3-4 months
- Key priority is to present a level of professionalism and look and feel on par with QR, Ferrander, Bramwell and Co, for people to know what I do and how to contact me.
- Link site to my linked in Profile
- My logo is attached and contact details
- I have purchased the domain name www.lumenassembly-example.com.au through true registries
Updates

Industry/Entity Type

Management Consulting

Coding

Coded - Design and coding required

Number of Pages Required

1 page

Requirements
Must have
• Mobile responsive to be viewed on any device, simple clean design, easy to find contact details, 3 scrolling articles like QR-example.com that link to a PDF article. Align colours and theming to Logo on white background attached. Align fonts, look and feel etc to Log design attached

```html
<!DOCTYPE html>
<html lang="en">
<head>
<meta charset="utf-8">
<title>LuMen Assembly — Powering Enterprise Renewal</title>
<link rel="stylesheet" href="https://fonts.googleapis.com/css2?family=Open+Sans:ital,wght@0,300;0,400;0,600;0,700;1,400&family=Montserrat:wght@600;700&family=PT+Serif:ital@1&display=swap">
<style>
:root{
  --blue:#29a3dc;
  --blue-deep:#1d6aa3;
  --black:#050505;
  --navy:#1a2540;
  --ink:#333a44;
  --muted:#8a8f96;
  --band:#f1f2f3;
  --line:#9fd3ee;
  --footer:#23262b;
  --footer-base:#1c1e22;
  --white:#ffffff;
}
*{box-sizing:border-box;margin:0;padding:0}
html,body{width:668px;height:1200px;overflow:hidden;background:var(--white)}
body{font-family:"Open Sans",Arial,sans-serif;color:var(--ink)}
.page{position:relative;width:668px;height:1200px;overflow:hidden}
.abs{position:absolute}

/* top bar + nav */
.topbar{left:0;top:0;width:668px;height:27px;background:var(--black)}
.search{left:455px;top:6px;width:133px;height:15px;border-bottom:1px solid #777;color:#ddd;font-size:7px;line-height:12px;padding-left:7px}
.search svg{position:absolute;right:2px;top:1px}
.nav{left:0;top:27px;width:668px;height:26px;background:var(--blue)}
.nav-link{top:36px;color:var(--white);font-size:7px;font-weight:700;text-transform:uppercase}
.social{top:36px;width:7px;height:7px;border-radius:50%;background:var(--white)}
.logo{left:80px;top:0;width:92px;height:62px;background:var(--white);display:flex;align-items:center;justify-content:center;gap:4px;z-index:3}
.logo-mark{width:6px;height:6px;border-radius:50%;background:var(--blue)}
.logo-name{font-size:9.5px;font-weight:600;color:var(--blue-deep);line-height:1.1;width:62px}

/* hero */
.hero{left:0;top:53px;width:668px;height:259px;background:linear-gradient(110deg,#101a38 0%,#2b3656 45%,#4b5777 70%,#222c4a 100%)}
.badge{background:var(--blue);color:var(--white);font-size:5.5px;font-weight:700;height:13px;line-height:13px;padding:0 6px}
.replies{color:#d6dbe6;font-size:5.5px;display:flex;align-items:center;gap:3px}
.hero-title{left:122px;top:133px;color:var(--white);font-size:24px;font-weight:700;letter-spacing:-.2px}
.hero-sub{left:124px;top:167px;color:var(--white);font-size:8.3px;font-weight:600;line-height:13px}
.btn-outline{left:124px;top:206px;width:83px;height:24px;border:1.5px solid var(--white);color:var(--white);font-size:8px;font-weight:700;text-align:center;line-height:21px}
.dot{left:576px;width:6px;height:6px;border-radius:50%;border:1px solid var(--white)}
.dot.on{background:var(--white)}

/* feature cards */
.card-photo{left:80px;top:330px;width:160px;height:156px;background:linear-gradient(180deg,#6d95c9 0%,#97b3d6 40%,#2e4d7d 70%,#1d3158 100%)}
.card-blue{left:254px;top:330px;width:159px;height:156px;background:linear-gradient(180deg,#27a0da 0%,#1e6fa6 100%)}
.card-title{color:var(--white);font-size:13.5px;font-weight:700;line-height:13.5px}
.card-text{color:#e6f2fa;font-size:6.8px;line-height:10.5px}
.profile{left:428px;top:279px;width:160px;height:207px;background:var(--white);border-top:3px solid var(--blue);box-shadow:0 1px 4px rgba(0,0,0,.18);text-align:center}
.avatar{position:absolute;left:47px;top:13px;width:66px;height:66px;border-radius:50%;background:linear-gradient(160deg,#6a6d72,#2a2b2f)}
.profile-name{position:absolute;left:0;top:86px;width:100%;font-size:14.5px;color:#444}
.profile-role{position:absolute;left:0;top:107px;width:100%;font-size:5.8px;font-weight:700;color:var(--blue);text-transform:uppercase}
.profile-bio{position:absolute;left:12px;top:122px;width:136px;font-size:7px;line-height:10px;color:#444}

/* newsletter */
.newsletter{left:0;top:504px;width:668px;height:44px;background:var(--band)}
.nl-label{left:80px;top:514px;font-size:8.5px;font-weight:700;letter-spacing:2px;line-height:11px;color:#222}
.field{top:516px;height:21px;background:var(--white);font-size:6.5px;letter-spacing:1px;color:#aaa;line-height:21px;padding-left:13px}
.btn-sub{left:481px;top:516px;width:107px;height:21px;background:var(--blue);color:var(--white);font-size:6.5px;letter-spacing:1.5px;text-align:center;line-height:21px}

/* tweet */
.rule{left:80px;width:334px;height:1px;background:var(--line)}
.tweet-mark{left:100px;top:607px;width:40px;height:40px;border-radius:50%;background:var(--blue)}
.tweet-handle{left:160px;top:607px;font-size:5.8px;font-weight:700;color:#333}
.tweet-quote{left:161px;top:626px;width:250px;font-family:"PT Serif",Georgia,serif;font-style:italic;font-size:10.3px;line-height:17px;color:#333}
.btn-follow{left:161px;top:689px;width:37px;height:12px;background:var(--blue);color:var(--white);font-size:5px;font-weight:700;font-style:italic;text-align:center;line-height:12px}

/* tabs */
.tabs{left:428px;top:566px;width:159px;height:178px;border:1px solid #eceef0}
.tab{top:566px;height:22px;font-size:6px;font-weight:700;line-height:22px;text-align:center;text-transform:uppercase}
.tab.active{background:var(--white);color:#222}
.tab.blue{background:var(--blue);color:var(--white)}
.post-thumb{left:436px;width:27px;height:24px;background:linear-gradient(180deg,#dfe3e8,#6c7580)}
.post-title{left:472px;font-size:6.3px;font-weight:700;line-height:8.5px;color:#333;width:112px}
.post-meta{left:472px;font-size:5px;color:#555}
.post-meta b{color:var(--blue);font-weight:600;margin-left:5px}

/* second hero */
.feature{left:0;top:764px;width:668px;height:252px;background:linear-gradient(100deg,#c9ccd1 0%,#9aa1ab 40%,#5b6472 75%,#3a4250 100%)}
.feature-box{left:80px;top:842px;width:261px;height:174px;background:rgba(35,32,30,.82)}
.feature-title{left:97px;top:860px;color:var(--white);font-size:27.5px;font-weight:300;line-height:32px}
.feature-text{left:98px;top:934px;width:200px;color:#eee;font-size:6.3px;line-height:10.5px}
.feature-more{left:98px;top:985px;color:var(--white);font-size:6.3px;font-weight:700}

/* footer */
.footer{left:0;top:1016px;width:668px;height:165px;background:var(--footer)}
.foot-head{top:1040px;font-family:"Montserrat",Arial,sans-serif;font-size:7.3px;font-weight:700;letter-spacing:.6px;color:var(--white)}
.foot-text{font-size:6.5px;line-height:11px;color:#cfd2d6;letter-spacing:.3px}
.foot-photo{left:80px;top:1089px;width:161px;height:65px;background:linear-gradient(90deg,#c7cacf,#eef0f2 60%,#d5d8dc)}
.foot-icon{width:5px;height:5px;background:#cfd2d6;border-radius:50%}
.foot-rule{left:428px;top:1109px;width:160px;height:1px;background:#4a4e55}
.base{left:0;top:1181px;width:668px;height:19px;background:var(--footer-base);color:#8b9098;font-size:5.8px;text-align:center;line-height:19px;letter-spacing:.4px}
</style>
</head>
<body>
<div class="page">

  <div class="abs topbar"></div>
  <div class="abs search">search
    <svg width="9" height="9" viewBox="0 0 10 10"><circle cx="4" cy="4" r="3" fill="none" stroke="#ddd" stroke-width="1.2"/><line x1="6.3" y1="6.3" x2="9" y2="9" stroke="#ddd" stroke-width="1.2"/></svg>
  </div>
  <div class="abs nav"></div>
  <div class="abs logo"><span class="logo-mark"></span><span class="logo-name">LuMen Assembly</span></div>
  <span class="abs nav-link" style="left:205px">Home</span>
  <span class="abs nav-link" style="left:250px">About us</span>
  <span class="abs nav-link" style="left:309px">Hot topics</span>
  <span class="abs nav-link" style="left:374px">Recent news</span>
  <span class="abs nav-link" style="left:446px">Contact us</span>
  <span class="abs social" style="left:521px"></span>
  <span class="abs social" style="left:540px"></span>
  <span class="abs social" style="left:559px"></span>
  <span class="abs social" style="left:580px"></span>

  <section class="abs hero" role="img" aria-label="Hand touching a tablet with glowing app icons floating above it"></section>
  <span class="abs badge" style="left:124px;top:118px">JUL 30, 2016</span>
  <span class="abs replies" style="left:179px;top:121px"><svg width="7" height="6" viewBox="0 0 8 7"><path d="M.5.5h7v4.5H3L1.5 6.5V5H.5z" fill="none" stroke="#d6dbe6" stroke-width=".8"/></svg>108 Replies</span>
  <h1 class="abs hero-title">Dealmaking in a digital world</h1>
  <p class="abs hero-sub">With the business world transforming, is it better to build or buy the capabilities you need?<br>We explore capital strategy for a digital future.</p>
  <a class="abs btn-outline">READ MORE</a>
  <span class="abs dot" style="top:166px"></span>
  <span class="abs dot" style="top:179px"></span>
  <span class="abs dot on" style="top:192px"></span>

  <article class="abs card-photo" role="img" aria-label="Wind turbines above a field of solar panels"></article>
  <h2 class="abs card-title" style="left:92px;top:421px">The new economics<br>of energy storage</h2>
  <span class="abs badge" style="left:88px;top:460px;background:#1f6fa8">JUL 30, 2016</span>
  <span class="abs replies" style="left:147px;top:463px"><svg width="7" height="6" viewBox="0 0 8 7"><path d="M.5.5h7v4.5H3L1.5 6.5V5H.5z" fill="none" stroke="#d6dbe6" stroke-width=".8"/></svg>82 Replies</span>

  <article class="abs card-blue"></article>
  <h2 class="abs card-title" style="left:265px;top:362px">The family business<br>competitive<br>advantage</h2>
  <p class="abs card-text" style="left:265px;top:408px;width:140px">In egestas nulla vitae nulla rhoncus, quis vulputate ipsum eleifend. Integer nibh est, porta at ultricies hendrerit, aliquam id metus.</p>
  <span class="abs badge" style="left:265px;top:460px;background:#1a4f7e">JUL 30, 2016</span>
  <span class="abs replies" style="left:321px;top:463px"><svg width="7" height="6" viewBox="0 0 8 7"><path d="M.5.5h7v4.5H3L1.5 6.5V5H.5z" fill="none" stroke="#d6dbe6" stroke-width=".8"/></svg>82 Replies</span>

  <aside class="abs profile">
    <div class="avatar" role="img" aria-label="Portrait of the founder"></div>
    <div class="profile-name">Rory Vance</div>
    <div class="profile-role">Founder LuMen Assembly</div>
    <p class="profile-bio">In egestas nulla vitae nulla rhoncus, quis vulputate ipsum eleifend. Integer nibh est, porta at ultricies hendrerit, aliquam id metus.&nbsp; Integer nibh est egestas nulla vitae nulla rhoncus, quis vulputate ipsum eleifend aliquam id metus.</p>
  </aside>

  <div class="abs newsletter"></div>
  <div class="abs nl-label">SIGNUP TO<br>NEWSLETTER</div>
  <div class="abs field" style="left:170px;width:146px">YOUR NAME</div>
  <div class="abs field" style="left:326px;width:145px">YOUR EMAIL ADDRESS</div>
  <div class="abs btn-sub">SUBSCRIBE NOW</div>

  <div class="abs rule" style="top:566px"></div>
  <div class="abs rule" style="top:744px"></div>
  <span class="abs tweet-mark"></span>
  <span class="abs tweet-handle">@RORYVANCE</span>
  <p class="abs tweet-quote">Aliquam tempus lectus sed nibh gravida, sed scelerisque enim vestibulum. Praesent at diam ut nisi ultrices adipiscing.</p>
  <span class="abs btn-follow">FOLLOW</span>

  <div class="abs tabs"></div>
  <span class="abs tab active" style="left:428px;width:50px">Popular</span>
  <span class="abs tab blue" style="left:478px;width:53px">Recent</span>
  <span class="abs tab blue" style="left:532px;width:55px">Top rated</span>

  <span class="abs post-thumb" style="top:598px" role="img" aria-label="Business people silhouettes"></span>
  <span class="abs post-title" style="top:596px">Lorem ipsum dolor sit amet,<br>consectetur adipiscing elit.</span>
  <span class="abs post-meta" style="top:615px">14 July 2016<b>19 Comments</b></span>
  <span class="abs post-thumb" style="top:634px" role="img" aria-label="Business people silhouettes"></span>
  <span class="abs post-title" style="top:632px">Lorem ipsum dolor sit amet,<br>consectetur adipiscing elit.</span>
  <span class="abs post-meta" style="top:651px">14 July 2016<b>19 Comments</b></span>
  <span class="abs post-thumb" style="top:669px" role="img" aria-label="Business people silhouettes"></span>
  <span class="abs post-title" style="top:667px">Lorem ipsum dolor sit amet,<br>consectetur adipiscing elit.</span>
  <span class="abs post-meta" style="top:686px">14 July 2016<b>19 Comments</b></span>
  <span class="abs post-thumb" style="top:705px" role="img" aria-label="Business people silhouettes"></span>
  <span class="abs post-title" style="top:703px">Lorem ipsum dolor sit amet,<br>consectetur adipiscing elit.</span>
  <span class="abs post-meta" style="top:722px">14 July 2016<b>19 Comments</b></span>

  <section class="abs feature" role="img" aria-label="Hand holding a stylus over a tablet"></section>
  <div class="abs feature-box"></div>
  <h2 class="abs feature-title">More power of<br>digital world.</h2>
  <p class="abs feature-text">Lorem ipsum dolor sit amet, consectetur adipiscing elit, sed do eiusmod tempor incididunt ut labore et dolore magna aliqua. Ut enim ad minim veniam, quis nostrud exercitation ullamco laboris nisi ut aliquip ex ea commodo consequat.</p>
  <span class="abs feature-more">read more &nbsp;→</span>

  <footer class="abs footer"></footer>
  <span class="abs foot-head" style="left:80px">ABOUT AUTHOR</span>
  <span class="abs foot-head" style="left:255px">LATEST TWEETS</span>
  <span class="abs foot-head" style="left:428px">LATEST COMMENT</span>

  <p class="abs foot-text" style="left:80px;top:1063px;width:170px">Lorem ipsum dolor sit amet, conser adipisicing esse cillum dolore nulla pariatur.</p>
  <div class="abs foot-photo" role="img" aria-label="Author portrait with hand-lettered name"></div>

  <span class="abs foot-icon" style="left:255px;top:1066px"></span>
  <p class="abs foot-text" style="left:265px;top:1063px">@brightlinnea</p>
  <p class="abs foot-text" style="left:265px;top:1078px;width:155px">Developer Advocate @morrowtess knows the very well is about things .</p>
  <span class="abs foot-icon" style="left:255px;top:1115px"></span>
  <p class="abs foot-text" style="left:265px;top:1112px">@brightlinnea</p>
  <p class="abs foot-text" style="left:265px;top:1127px;width:155px">Developer Advocate hav a great work this knows the very well is about things .</p>

  <p class="abs foot-text" style="left:428px;top:1063px">From Tobin :</p>
  <p class="abs foot-text" style="left:428px;top:1078px;width:160px">Developer Advocate @morrowtess know the very well is talking about things .</p>
  <div class="abs foot-rule"></div>
  <p class="abs foot-text" style="left:428px;top:1120px">From Mara Quell :</p>
  <p class="abs foot-text" style="left:428px;top:1135px;width:160px">Developer Advocate @morrowtess know the very well is talking about things .</p>

  <div class="abs base">@2016 COPYRIGHT. ALL RIGHT RESERVED &nbsp; | &nbsp; TERMS POLICY &nbsp; | &nbsp; DISCLAIMER</div>
</div>
</body>
</html>
```